R&T Photography (business cards)

Business cards for a photography business. We also photographs events, portraits, headshots.
Colors: Vanilla w/ dark blue (not Aqua or Navy)
Website: randtphotography482-mailbox.net
Email: randtphotography76@mailbox.net
Company Name: R&T Photography
Letter style/font for company name is French Script
We would like a card that somehow delivers a combination of softness, confidence and strength.

Target Market(s)

Wedding clients

Industry/Entity Type

Business

Font styles to use
Decorative
Script

Colors
0d5ba7
3176b5
5c5c5c
dbdbdb

Requirements
Must have
• Bold and/or raised print for company name. Website should also stand out. Telephone contact numbers are:
• (555) 214-7730
• (555) 862-3046
• Website: RandTPhotohraphy482-mailbox.net
• Business address: PO Box 6204, Orlando, FL 32899
• Back of card should state: referrals are welcome.
Nice to have
• some lace/scroll
Should not have
• Non-metallic.

```html
<!DOCTYPE html>
<html lang="en">
<head>
<meta charset="utf-8">
<title>R&amp;T Photography — Business Cards</title>
<link rel="stylesheet" href="https://fonts.googleapis.com/css2?family=Pinyon+Script&family=Cormorant+Garamond:wght@500;600;700&display=swap">
<style>
  :root {
    --backdrop: #e9e6df;
    --vanilla: #f7f0d9;
    --vanilla-deep: #efe4c2;
    --royal: #0d5ba7;
    --royal-dark: #0b3f86;
    --royal-light: #3176b5;
    --cream-ink: #f3ecd6;
    --shadow: rgba(30, 30, 40, 0.28);
  }
  * { box-sizing: border-box; margin: 0; padding: 0; }
  html, body { width: 1200px; height: 1023px; overflow: hidden; }
  body {
    background: var(--backdrop);
    position: relative;
    font-family: "Cormorant Garamond", Georgia, serif;
  }
  .card {
    position: absolute;
    width: 620px;
    height: 360px;
    border-radius: 6px;
    box-shadow: 0 14px 30px var(--shadow);
    overflow: hidden;
  }

  /* Front */
  .card-front {
    left: 70px; top: 90px;
    background: var(--royal-dark);
    padding: 8px;
  }
  .front-face {
    width: 100%; height: 100%;
    border-radius: 3px;
    background: radial-gradient(ellipse at 50% 45%, var(--vanilla) 55%, var(--vanilla-deep) 100%);
    display: flex;
    flex-direction: column;
    align-items: center;
    justify-content: center;
    text-align: center;
    color: var(--royal);
    padding: 0 20px;
  }
  .front-emblem {
    display: flex; align-items: center; gap: 10px;
    margin-bottom: 4px;
  }
  .emblem-circle {
    width: 58px; height: 58px; border-radius: 50%;
    background: var(--royal);
  }
  .emblem-name {
    font-family: "Cormorant Garamond", Georgia, serif;
    font-weight: 600;
    font-size: 24px;
    color: var(--royal);
  }
  .company-name {
    font-family: "Pinyon Script", "Brush Script MT", cursive;
    font-weight: 400;
    font-size: 52px;
    line-height: 1.15;
  }
  .tagline {
    font-variant: small-caps;
    font-weight: 600;
    font-size: 20px;
    letter-spacing: 0.5px;
    margin-top: 2px;
  }
  .phones { font-size: 17px; font-weight: 600; margin-top: 14px; }
  .details { font-size: 15px; font-weight: 600; margin-top: 3px; }
  .website {
    font-weight: 700;
    font-size: 22px;
    margin-top: 8px;
    letter-spacing: 0.3px;
  }

  /* Back */
  .card-back {
    left: 510px; top: 570px;
    background: linear-gradient(135deg, var(--royal-light) 0%, var(--royal) 40%, var(--royal-dark) 100%);
    border: 5px solid var(--vanilla-deep);
  }
  .back-ornament {
    position: absolute;
    left: 50%; top: 50%;
    width: 230px; height: 230px;
    transform: translate(-50%, -50%);
  }
  .back-emblem {
    position: absolute;
    left: 50%; top: 50%;
    transform: translate(-50%, -50%);
    display: flex; align-items: center; gap: 10px;
  }
  .back-emblem .emblem-circle {
    width: 110px; height: 110px;
    background: var(--cream-ink);
  }
  .back-emblem .emblem-name { color: var(--cream-ink); font-size: 28px; }
  .referrals {
    position: absolute;
    left: 26px; top: 22px;
    color: var(--cream-ink);
    font-size: 19px;
    font-weight: 600;
    letter-spacing: 0.5px;
  }
</style>
</head>
<body>

  <section class="card card-front" aria-label="Business card front">
    <div class="front-face">
      <div class="front-emblem">
        <div class="emblem-circle"></div>
        <span class="emblem-name">R&amp;T</span>
      </div>
      <h1 class="company-name">R&amp;T Photography</h1>
      <p class="tagline">Moments of Happiness, A Lifetime of Memories</p>
      <p class="phones">(555) 214-7730 &bull; (555) 862-3046</p>
      <p class="details">randtphotography76@mailbox.net &bull; PO Box 6204, Orlando, FL 32899</p>
      <p class="website">RandTPhotohraphy482-mailbox.net</p>
    </div>
  </section>

  <section class="card card-back" aria-label="Business card back">
    <svg class="back-ornament" viewBox="0 0 230 230" role="img" aria-label="Ornate scrollwork frame surrounding the emblem">
      <defs>
        <radialGradient id="ornamentGlow" cx="50%" cy="50%" r="50%">
          <stop offset="0%" stop-color="#f3ecd6" stop-opacity="0.35"/>
          <stop offset="100%" stop-color="#f3ecd6" stop-opacity="0"/>
        </radialGradient>
      </defs>
      <circle cx="115" cy="115" r="115" fill="url(#ornamentGlow)"/>
    </svg>
    <div class="back-emblem">
      <div class="emblem-circle"></div>
      <span class="emblem-name">R&amp;T</span>
    </div>
    <p class="referrals">Referrals Are Welcome</p>
  </section>

</body>
</html>
```